Business Card Design Project

for a second hand vintage clothing store. shop name is The Velvet Cupboard

Cards to be double sided

The name on the card is Joanna Whitfield

Information to put on card:

The Velvet Cupboard
Joanna Whitfield (no job title)
42/871 Dunmore St, Glenwick, Sydney, NSW, 2009.
Mobile: 0412 905 261
Email: thevelvetcupboard@mailbox.com.au
Web: www.thevelvetcupboard.com.au

Target Market(s)

Women looking at vintage clothing

Industry/Entity Type

Clothing

```html
<!DOCTYPE html>
<html lang="en">
<head>
<meta charset="utf-8">
<title>The Velvet Cupboard — Business Card</title>
<link rel="stylesheet" href="https://fonts.googleapis.com/css2?family=Noto+Serif:ital,wght@0,400;1,400;1,700&display=swap">
<style>
  :root {
    --plum: #58232f;
    --cream: #ecd896;
    --backdrop: #ededed;
    --card-w: 900px;
    --card-h: 520px;
  }
  * { box-sizing: border-box; margin: 0; padding: 0; }
  html, body {
    width: 1164px;
    height: 1200px;
    overflow: hidden;
    background: var(--backdrop);
    font-family: "Noto Serif", Georgia, serif;
  }
  .sheet {
    position: relative;
    width: 1164px;
    height: 1200px;
  }
  .card {
    position: absolute;
    left: 132px;
    width: var(--card-w);
    height: var(--card-h);
    background: var(--plum);
    border-radius: 30px;
    overflow: hidden;
    box-shadow: 0 6px 14px rgba(0,0,0,0.25);
  }
  .card--front { top: 60px; }
  .card--back  { top: 620px; }
  .card__bands {
    position: absolute;
    inset: 0;
    width: 100%;
    height: 100%;
  }
  .card__bands polygon { fill: var(--cream); }

  .brand-name {
    position: absolute;
    color: var(--cream);
    font-weight: 400;
    font-style: normal;
    white-space: nowrap;
    letter-spacing: 0.5px;
  }
  .card--front .brand-name {
    top: 32px;
    left: 170px;
    font-size: 46px;
  }
  .card--back .brand-name {
    top: 0;
    left: 0;
    width: 100%;
    line-height: var(--card-h);
    text-align: center;
    font-size: 70px;
  }

  .holder-name {
    position: absolute;
    top: 154px;
    left: 48px;
    font-size: 46px;
    font-weight: 700;
    font-style: italic;
    color: var(--plum);
    white-space: nowrap;
  }

  .contact-list {
    position: absolute;
    top: 245px;
    left: 36px;
    list-style: none;
  }
  .contact-list li {
    display: flex;
    align-items: center;
    gap: 14px;
    height: 54px;
    color: var(--cream);
    font-style: italic;
    font-size: 24px;
    white-space: nowrap;
  }
  .contact-list svg { width: 28px; height: 28px; flex: none; }
  .contact-list .icon-stroke { fill: none; stroke: var(--cream); stroke-width: 2; }

  .web-address {
    position: absolute;
    top: 400px;
    left: 150px;
    display: flex;
    align-items: center;
    gap: 22px;
    height: 56px;
    font-size: 40px;
    font-weight: 700;
    font-style: italic;
    color: var(--plum);
    white-space: nowrap;
  }
  .web-address svg { width: 40px; height: 40px; }
  .web-address .icon-stroke { fill: none; stroke: var(--plum); stroke-width: 2; }
</style>
</head>
<body>
<main class="sheet">

  <section class="card card--front" aria-label="Card front">
    <svg class="card__bands" viewBox="0 0 900 520" preserveAspectRatio="none" aria-hidden="true">
      <polygon points="0,146 575,146 632,188 575,230 0,230"/>
      <polygon points="100,428 142,398 900,398 900,456 142,456"/>
      <polygon points="500,520 558,464 900,464 900,520"/>
    </svg>

    <div class="brand-name">The Velvet Cupboard</div>
    <div class="holder-name">Joanna Whitfield</div>

    <ul class="contact-list">
      <li>
        <svg viewBox="0 0 28 28" aria-hidden="true">
          <rect class="icon-stroke" x="7" y="4" width="16" height="20" rx="2"/>
          <line class="icon-stroke" x1="4" y1="9" x2="9" y2="9"/>
          <line class="icon-stroke" x1="4" y1="14" x2="9" y2="14"/>
          <line class="icon-stroke" x1="4" y1="19" x2="9" y2="19"/>
        </svg>
        <span>42/871 Dunmore St, Glenwick, Sydney, NSW, 2009.</span>
      </li>
      <li>
        <svg viewBox="0 0 28 28" aria-hidden="true">
          <rect class="icon-stroke" x="8" y="3" width="13" height="22" rx="3"/>
          <line class="icon-stroke" x1="12" y1="21" x2="17" y2="21"/>
        </svg>
        <span>0412 905 261.</span>
      </li>
      <li>
        <svg viewBox="0 0 28 28" aria-hidden="true">
          <rect class="icon-stroke" x="3" y="8" width="22" height="14"/>
          <polyline class="icon-stroke" points="3,8 14,16 25,8"/>
        </svg>
        <span>thevelvetcupboard@mailbox.com.au</span>
      </li>
    </ul>

    <div class="web-address">
      <svg viewBox="0 0 40 40" aria-hidden="true">
        <circle class="icon-stroke" cx="20" cy="20" r="17"/>
        <ellipse class="icon-stroke" cx="20" cy="20" rx="8" ry="17"/>
        <line class="icon-stroke" x1="3" y1="20" x2="37" y2="20"/>
        <line class="icon-stroke" x1="6" y1="11" x2="34" y2="11"/>
        <line class="icon-stroke" x1="6" y1="29" x2="34" y2="29"/>
      </svg>
      <span>www.thevelvetcupboard.com.au</span>
    </div>
  </section>

  <section class="card card--back" aria-label="Card back">
    <svg class="card__bands" viewBox="0 0 900 520" preserveAspectRatio="none" aria-hidden="true">
      <polygon points="0,0 440,0 388,52 0,52"/>
      <polygon points="500,520 552,468 900,468 900,520"/>
    </svg>
    <div class="brand-name">The Velvet Cupboard</div>
  </section>

</main>
</body>
</html>
```